Business Card Design Project

need some business cards with the logo provided. I am a manufacturing jeweller that make high end quality jewellery in silver, gold and platinum and some amazing colored stones and of course diamonds.
Updates

Project Deadline Extended
Reason: I didn't choose this specific deadline and not sure why it was so short. A team member of craft hive helped as i am not the best on computers. (-: (wasn't asked about the dead line)

Target Market(s)

Adults based between 20 to 60 and have budgets between $5000 - $100 000

Industry/Entity Type

Business

Colors

Designer to choose colors to be used in the design.

Requirements
Must have
• All in the front of business card
LOGO provided
My name: Marisol Kettering
Job: Manufacturing jeweller
Phone number: 047 215 3904
Email: ketmar@quillnet.example and the chatterbook logo
this all in the back:
description of what i do : Hand Made Jewellery
new designs, remodelling, bridal jewellery, pearl re-threading and repairs
PO Box 5817, Kestrel Bay, 6391
Should not have
• Any diamond shapes or diamond rings or gemstones.

```html
<!DOCTYPE html>
<html lang="en">
<head>
<meta charset="utf-8">
<title>Velora Jewellers – Business Card</title>
<link href="https://fonts.googleapis.com/css2?family=Montserrat:wght@400;500&family=Great+Vibes&display=swap" rel="stylesheet">
<style>
  :root {
    --page: #ffffff;
    --card: #1f2023;
    --card-sheen: #55565a;
    --ink: #ffffff;
    --ink-muted: #a3a5a9;
    --brand: #b8bfc4;
    --ornament-a: #3a3b40;
    --ornament-b: #2a2b2f;
    --icon-box: #9a9ea3;
  }
  * { box-sizing: border-box; margin: 0; padding: 0; }
  html, body {
    width: 1000px; height: 1200px; overflow: hidden;
    background: var(--page);
    font-family: "Montserrat", Arial, sans-serif;
  }
  .canvas { position: relative; width: 1000px; height: 1200px; }

  .card {
    position: absolute;
    width: 760px; height: 462px;
    background: var(--card);
    overflow: hidden;
  }
  .card--front {
    left: 122px; top: 132px;
    background: linear-gradient(125deg, var(--card-sheen) 0%, #34353a 14%, var(--card) 34%, var(--card) 100%);
  }
  .card--back {
    left: 123px; top: 612px;
    background: linear-gradient(55deg, var(--card-sheen) 0%, #36373b 16%, var(--card) 36%, var(--card) 100%);
  }

  .floral { position: absolute; top: 0; right: 0; }
  .card--front .floral {
    width: 290px; height: 462px;
    background: radial-gradient(ellipse at 75% 45%, var(--ornament-a) 0%, var(--ornament-b) 55%, transparent 80%);
  }
  .card--back .floral {
    width: 290px; height: 440px; top: 22px;
    background: radial-gradient(ellipse at 70% 55%, var(--ornament-a) 0%, var(--ornament-b) 55%, transparent 80%);
  }

  .brand {
    position: absolute; left: 68px; top: 68px;
    width: 300px; text-align: center;
    color: var(--brand); font-weight: 400;
  }
  .brand__name { font-size: 60px; letter-spacing: 6px; line-height: 1; }
  .brand__tag { font-size: 19px; letter-spacing: 10px; margin-top: 24px; margin-right: -10px; }

  .person {
    position: absolute; right: 93px; top: 214px;
    text-align: right;
  }
  .person__name {
    font-family: "Great Vibes", cursive;
    font-size: 37px; color: var(--ink); line-height: 1;
    margin-bottom: 20px;
  }
  .person__role {
    font-size: 17px; color: var(--ink-muted);
    line-height: 18px; letter-spacing: 0.5px;
  }
  .rule { position: absolute; width: 3px; background: var(--ink); }
  .card--front .rule { left: 688px; top: 211px; height: 97px; }
  .card--back .rule { left: 85px; top: 100px; height: 97px; }

  .contact {
    position: absolute; left: 86px; top: 368px;
    font-size: 15.5px; line-height: 19px; color: var(--ink);
  }
  .contact__label { color: var(--ink-muted); }

  .social {
    position: absolute; left: 334px; top: 375px;
    display: flex; align-items: center; gap: 10px;
    font-size: 13px; color: var(--ink);
  }
  .social__box { width: 36px; height: 36px; background: var(--icon-box); }

  .services {
    position: absolute; left: 100px; top: 102px;
    font-size: 17.5px; line-height: 18.5px; color: var(--ink);
    text-transform: uppercase;
  }
  .address {
    position: absolute; right: 99px; top: 360px;
    font-size: 17px; color: var(--ink-muted); letter-spacing: 0.3px;
  }
</style>
</head>
<body>
<main class="canvas">
  <section class="card card--front">
    <div class="floral" role="img" aria-label="Decorative floral vine pattern in dark grey"></div>

    <div class="brand">
      <div class="brand__name">VELORA</div>
      <div class="brand__tag">JEWELLERS</div>
    </div>

    <div class="person">
      <div class="person__name">Marisol Kettering</div>
      <div class="person__role">MANUFACTURING<br>JEWELLER</div>
    </div>
    <div class="rule"></div>

    <div class="contact">
      <div><span class="contact__label">P:</span> 047 215 3904</div>
      <div><span class="contact__label">E:</span> ketmar@quillnet.example</div>
    </div>
    <div class="social">
      <span class="social__box"></span>
      <span>chatterbook</span>
    </div>
  </section>

  <section class="card card--back">
    <div class="floral" role="img" aria-label="Decorative floral vine pattern in dark grey"></div>
    <div class="rule"></div>
    <div class="services">
      Hand made jewellery<br>
      New designs, remodelling,<br>
      Bridal jewellery,<br>
      Pearl re-threading<br>
      and repairs
    </div>
    <div class="address">PO BOX 5817, KESTREL BAY, 6391</div>
  </section>
</main>
</body>
</html>
```